BSC Flyer to attract applicants 11x17

Brightline Stagecraft Company provides crew for local concerts, filming, theater, and corporate events.
The flyer will be posted on bulletin boards at colleges with theater programs.
Our primary venues are historic theaters in downtown LA
Need a 11x17 poster to attract potential applicants/crew
I have attached a poster that one of our staff made that has all if the relevant info - but i know the poster can look much better than that. I have also attached many images and our logo. It is not necessary to use all of the images, or any of them. The two images of the theater interiors are the venues we operate so they would be the first to include. I can send additional info or images upon request. Thank you

Entertainment

• APPLY@BSCCREWHUB.LA

```html
<!DOCTYPE html>
<html lang="en">
<head>
<meta charset="UTF-8">
<title>Brightline Stagecraft Company – We're Hiring Technicians</title>
<link href="https://fonts.googleapis.com/css2?family=Poppins:ital,wght@0,500;0,600;0,700;1,300;1,400;1,700;1,800;1,900&display=swap" rel="stylesheet">
<style>
  :root {
    --backdrop: #b6c3cd;
    --paper: #ffffff;
    --navy: #0a1433;
    --night: #10205a;
    --royal: #0a4fb5;
    --chevron: #e3e3e5;
    --ink: #111827;
  }
  * { box-sizing: border-box; margin: 0; padding: 0; }
  html, body {
    width: 1200px; height: 900px; overflow: hidden;
    background: var(--backdrop);
    font-family: "Poppins", sans-serif;
  }
  .poster {
    position: absolute; left: 322px; top: 20px;
    width: 556px; height: 860px;
    background: var(--paper);
    box-shadow: 0 10px 30px rgba(20, 35, 60, 0.25);
    overflow: hidden;
    text-align: center;
  }
  .hero { position: relative; display: block; width: 556px; height: 360px; }
  .brand {
    position: absolute; left: 168px; top: 26px;
    display: flex; align-items: center; gap: 8px;
    color: var(--paper);
    font-weight: 600; font-size: 11px; letter-spacing: 0.5px;
  }
  .brand-dot {
    width: 26px; height: 26px; border-radius: 50%;
    border: 2px solid var(--paper);
  }
  .headline {
    position: relative;
    color: var(--navy);
    font-style: italic; font-weight: 900;
    line-height: 0.92;
  }
  .headline-were { font-size: 116px; letter-spacing: -5px; margin-top: -48px; }
  .headline-hiring { font-size: 124px; letter-spacing: -6px; margin-left: -8px; }
  .role {
    width: 360px; margin: 14px auto 0;
    border-top: 2px solid var(--royal);
    border-bottom: 2px solid var(--royal);
    padding: 8px 0 6px;
    display: flex; align-items: center; justify-content: center; gap: 10px;
    color: var(--royal);
    font-style: italic; font-weight: 800; font-size: 40px; letter-spacing: -1.5px;
    line-height: 1.1;
  }
  .role-tick { width: 42px; height: 42px; flex: none; }
  .pitch {
    margin-top: 20px;
    color: var(--ink);
    font-style: italic; font-weight: 300; font-size: 20px; line-height: 1.3;
  }
  .apply-band {
    margin-top: 14px;
    background: var(--royal);
    color: var(--paper);
    font-style: italic; font-weight: 300; font-size: 20px;
    padding: 6px 0;
  }
  .apply-band strong { font-weight: 700; }
  .site {
    margin-top: 12px;
    color: var(--royal);
    font-style: italic; font-weight: 700; font-size: 11px; letter-spacing: 2.5px;
  }
</style>
</head>
<body>
  <main class="poster">
    <svg class="hero" viewBox="0 0 556 360" aria-hidden="false">
      <defs>
        <linearGradient id="skyline" x1="0" y1="0" x2="0" y2="1">
          <stop offset="0" stop-color="#10205a"/>
          <stop offset="0.6" stop-color="#2a3c8a"/>
          <stop offset="1" stop-color="#5a4a6a"/>
        </linearGradient>
        <linearGradient id="theatre" x1="0" y1="0" x2="1" y2="1">
          <stop offset="0" stop-color="#6a2a20"/>
          <stop offset="0.5" stop-color="#a8642a"/>
          <stop offset="1" stop-color="#3a1a5a"/>
        </linearGradient>
        <linearGradient id="console" x1="0" y1="0" x2="1" y2="1">
          <stop offset="0" stop-color="#3a4a6a"/>
          <stop offset="0.5" stop-color="#a8b4c8"/>
          <stop offset="1" stop-color="#2a2e3a"/>
        </linearGradient>
        <linearGradient id="stagelights" x1="0" y1="1" x2="1" y2="0">
          <stop offset="0" stop-color="#4a3ad0"/>
          <stop offset="0.5" stop-color="#8a7af0"/>
          <stop offset="1" stop-color="#2a2a6a"/>
        </linearGradient>
      </defs>
      <polygon class="chevron" points="50,0 556,0 556,50 230,380" fill="var(--chevron)"/>
      <polygon role="img" aria-label="Downtown Los Angeles skyline at night" points="140,0 510,0 460,70 400,70 230,300" fill="url(#skyline)"/>
      <polygon role="img" aria-label="Historic theater interior with ornate walls and seating" points="0,100 97,100 211,340 0,340" fill="url(#theatre)"/>
      <polygon role="img" aria-label="Audio mixing console" points="492,115 556,115 556,215 393,215" fill="url(#console)"/>
      <polygon role="img" aria-label="Stage lighting rig under purple light" points="383,225 540,225 540,345 264,345" fill="url(#stagelights)"/>
    </svg>
    <div class="brand">
      <span class="brand-dot"></span>
      <span class="brand-name">BRIGHTLINE STAGECRAFT COMPANY</span>
    </div>

    <h1 class="headline">
      <div class="headline-were">We’re</div>
      <div class="headline-hiring">HIRING</div>
    </h1>

    <h2 class="role">
      <svg class="role-tick" viewBox="0 0 42 42">
        <rect x="3" y="3" width="36" height="36" rx="3" fill="none" stroke="var(--royal)" stroke-width="3.5"/>
        <polyline points="11,21 18,28 31,13" fill="none" stroke="var(--royal)" stroke-width="4" stroke-linecap="round" stroke-linejoin="round"/>
      </svg>
      TECHNICIANS
    </h2>

    <p class="pitch">We are looking for talented<br>technicians to add to our roster<br>of skilled professionals.</p>

    <p class="apply-band">Send Resume to: <strong>apply@bsccrewhub.la</strong></p>

    <p class="site">WWW.BSCCREWHUB.LA</p>
  </main>
</body>
</html>
```